New boutique hotel for tourists, with hint of art deco styling

This is a new, soon to be completed, boutique hotel in Sydney. A letterhead with a logo is required. Less emphasis on the word "boutique". Perhaps the word could be screened to be lighter in colour (or print intensity). Would like a simple, clear, easy-to read, sans serif type face. The information on the letterhead is:
Mrs Perrow Boutique Hotel
418 Calloway Street,
Wrenfield, NSW, 2094
Australia
Tel: +61 2 9478-0000
mrsperrowhotel@example-mail.com
mrsperrowhotel.com.au
ABN 47 902 365 118

Target Market(s)

travellers, tourists, various ages

Industry/Entity Type

Hospitality

Contact Information for Business Card

Mrs Perrow Boutique Hotel
418 Calloway Street,
Wrenfield, NSW, 2094
Telephone: (02) 9478-0000
www.mrsperrowhotel.com.au
mrsperrowhotel@example-mail.com
ABN 47 902 365 118

Logo Text

suggest playing with the letter "B"

Font styles to use
Sans Serif

Colors
3176b5

Requirements
Must have
• ABN to be very small.
• Must be clear, easy to read and in a sans serif typeface, please!
Nice to have
• The word "Boutique" should be less intense in appearance to the rest of the name, or even "Boutique Hotel" can have less prominence than "Mrs Perrow".
Should not have
• No serif typeface. Sans serif only will be accepted.

```html
<!DOCTYPE html>
<html lang="en">
<head>
<meta charset="utf-8">
<title>Mrs Perrow Boutique Hotel – Stationery</title>
<link rel="stylesheet" href="https://fonts.googleapis.com/css2?family=Montserrat:wght@500&family=Open+Sans:wght@400&display=swap">
<style>
  :root{
    --navy:#0c2542;
    --paper:#ffffff;
    --stage:#9b9b9b;
    --ink:#3a3f47;
    --soft:#c9d3df;
  }
  *{margin:0;padding:0;box-sizing:border-box}
  html,body{width:1200px;height:1200px;overflow:hidden}
  body{background:var(--stage);position:relative;font-family:"Open Sans",sans-serif;color:var(--ink)}

  .hotel-name{font-family:"Montserrat",sans-serif;font-weight:500;color:var(--navy);text-align:center;text-transform:uppercase;line-height:1}
  .hotel-name .main{display:block}
  .hotel-name .sub{display:block;letter-spacing:.32em}

  /* Letterhead */
  .letterhead{position:absolute;left:241px;top:368px;width:342px;height:452px;background:var(--paper)}
  .letterhead .hotel-name{margin-top:22px}
  .letterhead .hotel-name .main{font-size:14px}
  .letterhead .hotel-name .sub{font-size:4.6px;margin-top:3px}
  .letter-body{position:absolute;left:20px;top:133px;width:300px;font-size:5.6px;line-height:1.75}
  .letter-body p{margin-bottom:7px}
  .letter-footer{position:absolute;left:0;bottom:0;width:100%;height:44px;background:var(--navy);padding:5px 20px}
  .letter-footer li{list-style:none;display:flex;align-items:center;gap:4px;color:#fff;font-size:3.6px;line-height:6.6px}
  .letter-footer svg{width:4.5px;height:4.5px}

  /* Business card front */
  .card-front{position:absolute;left:634px;top:372px;width:326px;height:188px;background:var(--navy);color:#fff}
  .card-front .hotel-name{color:#fff;margin-top:66px}
  .card-front .main{font-size:29px}
  .card-front .sub{font-size:10px;margin-top:4px;color:var(--soft)}
  .card-front .web{position:absolute;bottom:24px;width:100%;text-align:center;font-size:6px;letter-spacing:.5em;color:var(--soft)}

  /* Business card back */
  .card-back{position:absolute;left:634px;top:619px;width:326px;height:191px;background:var(--paper);overflow:hidden}
  .card-back .hotel-name{margin-top:34px}
  .card-back .main{font-size:27px}
  .card-back .sub{font-size:9.4px;margin-top:4px}
  .card-wave{position:absolute;left:0;top:0;width:326px;height:191px}
  .card-contact{position:absolute;left:18px;top:123px;color:#fff;font-size:5.4px}
  .card-contact li{list-style:none;display:flex;align-items:flex-start;gap:5px;margin-bottom:5px;line-height:6.6px}
  .card-contact svg{width:8px;height:8px;flex:none}
  .card-abn{position:absolute;right:14px;top:168px;color:#fff;font-size:4.6px;letter-spacing:.28em}
</style>
</head>
<body>

<svg width="0" height="0" style="position:absolute" aria-hidden="true">
  <defs>
    <symbol id="i-pin" viewBox="0 0 10 10"><rect width="10" height="10" rx="1.5" fill="#fff"/><path d="M5 2a2 2 0 0 1 2 2c0 1.5-2 4-2 4S3 5.5 3 4a2 2 0 0 1 2-2z" fill="#0c2542"/></symbol>
    <symbol id="i-phone" viewBox="0 0 10 10"><rect width="10" height="10" rx="1.5" fill="#fff"/><path d="M3 2.2l1.2 1.6-.6.8c.4.9 1 1.5 1.8 1.9l.8-.6L7.8 7 7 7.9C4.6 7.6 2.4 5.4 2.1 3z" fill="#0c2542"/></symbol>
    <symbol id="i-mail" viewBox="0 0 10 10"><rect width="10" height="10" rx="1.5" fill="#fff"/><rect x="2.2" y="3" width="5.6" height="4" fill="none" stroke="#0c2542" stroke-width=".8"/><path d="M2.2 3l2.8 2.2L7.8 3" fill="none" stroke="#0c2542" stroke-width=".8"/></symbol>
    <symbol id="i-web" viewBox="0 0 10 10"><rect width="10" height="10" rx="1.5" fill="#fff"/><circle cx="5" cy="5" r="2.7" fill="none" stroke="#0c2542" stroke-width=".8"/><path d="M2.3 5h5.4M5 2.3c-1.4 1.6-1.4 3.8 0 5.4M5 2.3c1.4 1.6 1.4 3.8 0 5.4" fill="none" stroke="#0c2542" stroke-width=".6"/></symbol>
  </defs>
</svg>

<section class="letterhead">
  <div class="hotel-name"><span class="main">Mrs Perrow</span><span class="sub">Boutique Hotel</span></div>
  <div class="letter-body">
    <p>Dear [Recipient],</p>
    <p>We love the look of this stationery just the way it is. But you can add your own personal touch in almost no time.</p>
    <p>On the Design tab of the ribbon, check out the Themes, Colors, and Fonts galleries to preview different looks from a variety of choices. Then just click to apply the one you like.</p>
    <p>We've also created styles that let you match the formatting you see in this letter with just a click. On the Home tab of the ribbon, check out the Styles gallery for all styles used in this letter.</p>
    <p>Ready to add your digits? No problem. Just double-click the header area to add your contact information.</p>
    <p>Warm regards,<br>Jordan</p>
  </div>
  <ul class="letter-footer">
    <li><svg><use href="#i-pin"/></svg>418 Calloway Street, Wrenfield, NSW, 2094 Australia</li>
    <li><svg><use href="#i-phone"/></svg>+61 2 9478-0000</li>
    <li><svg><use href="#i-mail"/></svg>mrsperrowhotel@example-mail.com</li>
    <li><svg><use href="#i-web"/></svg>mrsperrowhotel.com.au</li>
  </ul>
</section>

<section class="card-front">
  <div class="hotel-name"><span class="main">Mrs Perrow</span><span class="sub">Boutique Hotel</span></div>
  <div class="web">mrsperrowhotel.com.au</div>
</section>

<section class="card-back">
  <div class="hotel-name"><span class="main">Mrs Perrow</span><span class="sub">Boutique Hotel</span></div>
  <svg class="card-wave" viewBox="0 0 326 191" aria-hidden="true">
    <path d="M0 98 C70 82 130 110 190 124 C240 136 290 128 326 104 L326 191 L0 191 Z" fill="#0c2542"/>
    <path d="M0 104 C70 90 130 118 190 132 C240 144 292 134 326 112" fill="none" stroke="#fff" stroke-width="2.4"/>
  </svg>
  <ul class="card-contact">
    <li><svg><use href="#i-pin"/></svg><span>418 Calloway Street, Wrenfield<br>NSW 2094 Australia</span></li>
    <li><svg><use href="#i-phone"/></svg>(02) 9478-0000</li>
    <li><svg><use href="#i-mail"/></svg>mrsperrowhotel@example-mail.com</li>
    <li><svg><use href="#i-web"/></svg>www.mrsperrowhotel.com.au</li>
  </ul>
  <div class="card-abn">ABN 47 902 365 118</div>
</section>

</body>
</html>
```